Business Card Design Project

Business card for new event planning company. I will load in 2 different colors of logs for you to use.

Target Market(s)

meeting planners and business leaders

Industry/Entity Type

Event Planning

Requirements
Must have
• memorable/ creative please - maybe logo on back of the card

Information for business card: (Information may change)

LaVonna Pettibrook
lav@MarigoldOccasionsandGalas.com
www.MarigoldOccasionsandGalas.com
613.275.9042
Nice to have
• Do you think it would be too much to add chirpy, QX, workmesh logo to card to connect?

all are LaVonna Pettibrook

```html
<!DOCTYPE html>
<html lang="en">
<head>
<meta charset="utf-8">
<title>Marigold Occasions &amp; Galas — Business Cards</title>
<link rel="stylesheet" href="https://fonts.googleapis.com/css2?family=Barlow:wght@400;600&display=swap">
<style>
  :root {
    --stage: #1c2630;
    --card: #1f1b1e;
    --lavender: #8f7fc4;
    --scarlet: #d8321f;
    --ink-strong: #8d8c8e;
    --ink-soft: #8a898b;
  }
  * { margin: 0; padding: 0; box-sizing: border-box; }
  html, body { width: 1200px; height: 1000px; overflow: hidden; }
  body {
    background: var(--stage);
    font-family: "Barlow", Arial, sans-serif;
    position: relative;
  }
  .card {
    position: absolute;
    width: 583px;
    height: 378px;
    background: var(--card);
    overflow: hidden;
  }
  .card--front { left: 17px; top: 130px; }
  .card--back { left: 580px; top: 560px; box-shadow: 0 0 40px rgba(255,255,255,0.12); }

  .band { position: absolute; left: 0; width: 100%; }
  .band--top { top: 0; height: 85px; background: linear-gradient(180deg, #9585c9, #7d6db4); }
  .band--bottom { bottom: 0; height: 88px; background: linear-gradient(180deg, #de3a25, #c52c1a); }

  .brand {
    position: absolute;
    display: flex;
    align-items: center;
    gap: 12px;
    color: var(--lavender);
    font-weight: 600;
    white-space: nowrap;
  }
  .brand__dot {
    width: 18px; height: 18px;
    border-radius: 50%;
    background: var(--lavender);
  }
  .card--front .brand { left: 0; right: 0; top: 168px; justify-content: center; font-size: 38px; }
  .card--back .brand { left: 100px; top: 70px; font-size: 34px; }

  .contact {
    position: absolute;
    left: 108px;
    top: 180px;
    list-style: none;
    font-size: 24px;
    line-height: 32px;
    color: var(--ink-soft);
  }
  .contact__name { font-weight: 600; color: var(--ink-strong); }
</style>
</head>
<body>
  <section class="card card--front" aria-label="Card front">
    <div class="band band--top" role="img" aria-label="Lavender hand-scribbled line band"></div>
    <div class="brand"><span class="brand__name">Marigold Occasions &amp; Galas</span><span class="brand__dot"></span></div>
    <div class="band band--bottom" role="img" aria-label="Red hand-scribbled line band"></div>
  </section>

  <section class="card card--back" aria-label="Card back">
    <div class="brand"><span class="brand__name">Marigold Occasions &amp; Galas</span><span class="brand__dot"></span></div>
    <ul class="contact">
      <li class="contact__name">LaVonna Pettibrook</li>
      <li class="contact__email">lav@MarigoldOccasionsandGalas.com</li>
      <li class="contact__web">www.MarigoldOccasionsandGalas.com</li>
      <li class="contact__phone">613.275.9042</li>
    </ul>
  </section>
</body>
</html>
```